Showcase Competition Event For Teenagers Needs Promo Graphics

I am in need of graphics for 2019 Brightwater Youth Showcase. It is a Showcase competition event for teenagers. I need graphics to make an 11x17 poster and a main title graphic that I can use for digital (social, 16x9 for screens, etc). Graphic should include the following 2 logos: the KV Rising Crew logo (this is who we are) and the "circles" logo is the logo of Youth Showcase so that can be incorporated but is not mandatory and does not need to be in color. Tag line for Showcase is "Discover. Develop. Deploy." Again, this is optional. Looking for an artistic design - geometric shapes, bright colors, or something along those lines. Something that speaks to teenagers and especially creatives/Showcase types. Additionally, Post should include:
Linwood Grace Hall
March 29-30
(registration & cost info may be added to the poster before design is finalized; still working on those details)

```html
<!DOCTYPE html>
<html lang="en">
<head>
<meta charset="utf-8">
<title>Youth Showcase — Poster</title>
<link href="https://fonts.googleapis.com/css2?family=Bebas+Neue&family=Barlow+Condensed:wght@600;700&family=Mulish:wght@300&display=swap" rel="stylesheet">
<style>
  :root {
    --paper: #f4f4f6;
    --red: #cb332b;
    --teal: #84b9bb;
    --overlap: #6d2420;
    --ink: #222222;
    --line: #6a6a6a;
    --grid: #7a7a7a;
    --sky: #22b4ee;
  }
  html, body {
    margin: 0;
    padding: 0;
    overflow: hidden;
    background: var(--paper);
  }
  .poster {
    position: relative;
    width: 964px;
    height: 1200px;
    overflow: hidden;
    background: var(--paper);
  }
  .shapes {
    position: absolute;
    inset: 0;
    width: 964px;
    height: 1200px;
  }
  .crew-name {
    position: absolute;
    left: 82px;
    top: 96px;
    margin: 0;
    font-family: "Barlow Condensed", sans-serif;
    font-weight: 700;
    font-size: 40px;
    line-height: 1;
    color: var(--sky);
  }
  .showcase-mark {
    position: absolute;
    left: 704px;
    top: 126px;
    width: 112px;
    margin: 0;
    text-align: center;
    font-family: "Barlow Condensed", sans-serif;
    font-weight: 600;
    font-size: 22px;
    line-height: 1.05;
    color: var(--ink);
  }
  .title {
    margin: 0;
    font-family: "Bebas Neue", sans-serif;
    font-weight: 400;
    line-height: 1;
  }
  .title-top {
    position: absolute;
    left: 75px;
    top: 214px;
    font-size: 106px;
    color: var(--red);
  }
  .title-main {
    position: absolute;
    left: 75px;
    top: 313px;
    font-size: 168px;
    color: var(--ink);
    white-space: nowrap;
  }
  .title-highlight {
    position: relative;
    z-index: 0;
    display: inline-block;
    line-height: 1;
    color: #ffffff;
  }
  .title-highlight::before {
    content: "";
    position: absolute;
    z-index: -1;
    left: -0.06em;
    right: 0.04em;
    top: 0.09em;
    height: 0.72em;
    background: var(--teal);
  }
  .event-date {
    position: absolute;
    left: 120px;
    top: 862px;
    margin: 0;
    font-family: "Barlow Condensed", sans-serif;
    font-weight: 600;
    font-size: 56px;
    line-height: 1;
    color: #111111;
  }
  .tagline {
    position: absolute;
    left: 120px;
    top: 922px;
    margin: 0;
    font-family: "Barlow Condensed", sans-serif;
    font-weight: 600;
    font-size: 34px;
    line-height: 1;
    color: #111111;
  }
  .venue {
    position: absolute;
    left: 0;
    right: 0;
    top: 1130px;
    margin: 0;
    text-align: center;
    font-family: "Mulish", sans-serif;
    font-weight: 300;
    font-size: 28px;
    line-height: 1;
    color: #111111;
  }
</style>
</head>
<body>
<main class="poster">
  <svg class="shapes" viewBox="0 0 1123 1400" preserveAspectRatio="none" aria-hidden="true">
    <!-- showcase mark ring -->
    <circle cx="885" cy="168" r="64" fill="none" stroke="var(--sky)" stroke-width="7"/>
    <!-- grid -->
    <g class="grid" stroke="var(--grid)" stroke-width="1.2" fill="none">
      <rect x="917" y="228" width="139" height="143"/>
      <line x1="940" y1="228" x2="940" y2="371"/>
      <line x1="963" y1="228" x2="963" y2="371"/>
      <line x1="986" y1="228" x2="986" y2="371"/>
      <line x1="1010" y1="228" x2="1010" y2="371"/>
      <line x1="1033" y1="228" x2="1033" y2="371"/>
      <line x1="917" y1="252" x2="1056" y2="252"/>
      <line x1="917" y1="276" x2="1056" y2="276"/>
      <line x1="917" y1="300" x2="1056" y2="300"/>
      <line x1="917" y1="323" x2="1056" y2="323"/>
      <line x1="917" y1="347" x2="1056" y2="347"/>
    </g>
    <!-- large triangles -->
    <polygon class="tri-red" points="555,262 795,677 315,677" fill="var(--red)"/>
    <polygon class="tri-teal" points="435,582 1056,582 746,1118" fill="var(--teal)"/>
    <polygon class="tri-overlap" points="435,582 740,582 795,677 490,677" fill="var(--overlap)"/>
    <!-- diagonal rays -->
    <g class="rays" stroke="var(--line)" stroke-width="2.6">
      <line x1="192" y1="973" x2="490" y2="677"/>
      <line x1="234" y1="973" x2="532" y2="677"/>
      <line x1="276" y1="973" x2="574" y2="677"/>
      <line x1="318" y1="973" x2="616" y2="677"/>
      <line x1="360" y1="973" x2="658" y2="677"/>
      <line x1="402" y1="973" x2="700" y2="677"/>
      <line x1="443" y1="973" x2="740" y2="677"/>
    </g>
    <!-- small triangle -->
    <polygon class="tri-small" points="637,981 717,1118 557,1118" fill="var(--red)"/>
  </svg>

  <p class="crew-name">KV Rising Crew</p>
  <p class="showcase-mark">Youth Showcase</p>

  <h1 class="title">
    <span class="title-top">Youth</span>
    <span class="title-main">Show<span class="title-highlight">case</span></span>
  </h1>

  <p class="event-date">29 - 30 MARCH</p>
  <p class="tagline">Discover. Develop. Deploy</p>

  <p class="venue">Linwood Grace Hall</p>
</main>
</body>
</html>
```